Post Card Notification - rental property registration

We need a post card mailer designed to notify Landlord's of the need to register their rental properties according to local ordinance. Designed for optimal response, the response we are looking for is getting the recipient to go to a URL that will be on the postcard.

The postcards will be sent on behalf on Municipalities (aka communities) that we represent. They notify the Homeowner/Landlord of the need to register their property. We will inform them of the properties we have discovered evidence and registration is required. We are considering a color post card that will include the community logo and the company logo and other formatting graphics that enhance the design to get the result we are looking for.

There will be dynamic content in the design that will be specific tothe community logo, message text, property addresses, URL/Code, etc...

Clarifications 9/10/2018:
I wanted to clarify that this post card is not an advertisement but rather an official notification of the obligation to comply and register the property. We want the design to be professional but not to look like an advertisement.

We are looking for instant credibility. This should come with a focus on the community logo. Whether or not we even show the VELTRIDANE logo is optional, I am open to designs without it.

Also, we want to emphasize getting them to the coded link.

None of the designs so far achieve the instant credibility or give enough focus to the getting them to the link.

Lastly, the property list will be an actual list of 1 to 5 properties that are required to be registered by the owner. The design should contemplate an actual list of properties.

If you need a sample community logo you can pull one from veltridane.example or from any U.S. community home page.

One other point of clarification, the postcard will be sent for one community at a time. I see some designs with multiple community logos and that is not accurate. If an owner has rental properties in multiple communities then they will get multiple postcards from us. Each post card will be unique to a specific community.

If the owner has multiple properties in that community then they will be listed (hence the property list of 1 to 5 properties)

Most of the designs I am reviewing have focused to much on making it look like an advertisement with property images. I wanted to clarify that this should look official. There will be a community logo on the post card. We may not even have the VELTRIDANE logo on the card, I am open to designs with or without it. Also, the property list will be a list of properties where evidence has been found that it is rented by the owner. We anticipate this will be 1 to 5 properties in a dynamic list. The design should contemplate this. We want the design to look professional but it does not need to look like an advertisement. It needs to get their attention, and have them instantly recognize it as official (instant credibility) and get them to go to the link. None of the designs so far give enough prominence to the community logo or link that I think will be necessary to achieve this goal.

Target Market(s)

Landlords of rented properties

Industry/Entity Type

Government

Requirements
Must have
• Must look official, from the communities that we are partnered with
Should not have
• This should not look like a Real Estate advertisement

```html
<!DOCTYPE html>
<html lang="en">
<head>
<meta charset="utf-8">
<title>Rental Registration Postcard</title>
<link rel="stylesheet" href="https://fonts.googleapis.com/css2?family=Saira+Condensed:wght@400;500;600;700&family=Black+Ops+One&display=swap">
<style>
  :root {
    --yellow: #ecb94b;
    --yellow-soft: #e9bf5c;
    --navy: #3b4250;
    --red: #c9403b;
    --ink: #2b2f36;
    --paper: #f1f1f0;
    --bg: #e4e4e2;
    --white: #ffffff;
  }
  * { box-sizing: border-box; margin: 0; padding: 0; }
  html, body { width: 1200px; height: 900px; overflow: hidden; }
  body {
    background: var(--bg);
    font-family: "Saira Condensed", "Arial Narrow", sans-serif;
    color: var(--ink);
    position: relative;
  }
  .postcard {
    position: absolute;
    width: 560px;
    height: 372px;
    top: 264px;
    overflow: hidden;
    box-shadow: 0 6px 18px rgba(0,0,0,0.18);
  }

  /* Front */
  .postcard--front { left: 30px; background: var(--yellow); }
  .front-notice { position: absolute; left: 0; top: 0; width: 322px; height: 341px; }
  .warning-stamp {
    position: absolute; left: 94px; top: 40px; width: 148px; height: 38px;
    border: 3px solid var(--red); border-radius: 3px;
    display: flex; align-items: center; justify-content: center;
    font-family: "Black Ops One", "Impact", sans-serif;
    color: var(--red); font-size: 25px; letter-spacing: 1px;
  }
  .fill-row {
    position: absolute; left: 43px; right: 10px;
    display: flex; align-items: flex-end; gap: 6px;
    font-size: 16px; line-height: 1;
  }
  .fill-row .rule { flex: 1; border-bottom: 1px solid var(--ink); height: 1px; margin-bottom: 2px; }
  .fill-row--per { top: 88px; }
  .fill-row--ordinance { top: 110px; }
  .requirement { position: absolute; left: 43px; top: 134px; font-size: 16px; line-height: 1.2; }
  .evidence-pill {
    position: absolute; left: 68px; top: 166px; width: 224px; height: 63px;
    background: var(--navy); border-radius: 14px;
    color: var(--yellow); font-size: 14.5px; line-height: 17px; text-align: center;
    display: flex; align-items: center; justify-content: center; padding: 0 8px;
  }
  .behalf { position: absolute; left: 71px; top: 246px; font-size: 16.5px; white-space: nowrap; }
  .behalf strong { font-weight: 700; }
  .behalf-rule { position: absolute; left: 48px; right: 0; top: 283px; border-bottom: 1px solid var(--ink); }
  .program { position: absolute; left: 0; width: 322px; top: 290px; text-align: center; font-size: 16.5px; line-height: 19px; }
  .program .accent { color: var(--white); }
  .front-divider { position: absolute; left: 322px; top: 0; width: 8px; height: 341px; background: var(--navy); }
  .front-photo {
    position: absolute; left: 330px; top: 0; width: 230px; height: 341px;
    background: linear-gradient(180deg, #7f98a6 0%, #8a9ba4 35%, #4a5058 60%, #a99c8e 100%);
  }
  .community-logo {
    position: absolute; right: 2px; top: 0; width: 140px; height: 136px;
    background: var(--navy);
    border-left: 5px solid var(--yellow); border-bottom: 5px solid var(--yellow);
    outline: 3px solid var(--white);
    display: flex; align-items: center; justify-content: center;
    color: var(--yellow); font-weight: 700; font-size: 24px; letter-spacing: 1px;
  }
  .front-footer {
    position: absolute; left: 0; bottom: 0; width: 100%; height: 31px;
    background: var(--navy); display: flex; align-items: center; gap: 8px; padding-left: 40px;
    font-size: 12.5px; color: var(--yellow); white-space: nowrap;
  }
  .front-footer .url { color: var(--white); font-weight: 700; font-size: 18px; letter-spacing: 0.5px; }

  /* Back */
  .postcard--back { left: 610px; background: var(--paper); }
  .back-photo {
    position: absolute; left: 0; top: 0; width: 401px; height: 316px;
    background: linear-gradient(180deg, #f4f4f3 0%, #e9e9e8 50%, #f6f6f5 100%);
  }
  .address-fields { position: absolute; left: 51px; top: 0; width: 335px; height: 316px; font-size: 14px; font-weight: 500; }
  .field { position: absolute; left: 0; right: 0; display: flex; align-items: flex-end; gap: 4px; line-height: 1; }
  .field .rule { flex: 1; border-bottom: 1px solid var(--ink); height: 1px; margin-bottom: 1px; }
  .field--property { top: 22px; }
  .property-list { position: absolute; left: 0; right: 0; top: 44px; list-style: none; font-size: 13px; }
  .property-list li { display: flex; align-items: flex-end; gap: 6px; height: 19px; line-height: 1; }
  .property-list .num { width: 12px; font-weight: 600; }
  .property-list .rule { flex: 1; border-bottom: 1px solid var(--ink); margin-bottom: 2px; }
  .field--owner { top: 160px; }
  .field--site { top: 195px; }
  .field--id { top: 230px; }
  .field--notice { top: 265px; }
  .back-side {
    position: absolute; left: 401px; top: 0; width: 159px; height: 316px;
    background: linear-gradient(180deg, var(--yellow-soft) 0%, var(--yellow) 55%, #d9a64a 100%);
  }
  .stamp-box { position: absolute; left: 422px; top: 42px; width: 96px; height: 91px; background: var(--white); border-radius: 8px; }
  .back-footer {
    position: absolute; left: 0; bottom: 0; width: 100%; height: 56px; background: var(--navy);
    color: var(--yellow); text-align: center; font-size: 13.5px; line-height: 21px; padding-top: 6px;
  }
  .back-footer .contact { color: var(--white); font-size: 16px; }
</style>
</head>
<body>
  <section class="postcard postcard--front" aria-label="Postcard front">
    <div class="front-notice">
      <div class="warning-stamp">WARNING</div>
      <div class="fill-row fill-row--per"><span class="label">Per</span><span class="rule"></span></div>
      <div class="fill-row fill-row--ordinance"><span class="label">Ordinance</span><span class="rule"></span></div>
      <p class="requirement">Rental Properties Requires Registration</p>
      <p class="evidence-pill">Evidence indicates that one or more properties that you own requires registration.</p>
      <p class="behalf"><strong>VELTRIDANE</strong> is working on behalf</p>
      <div class="behalf-rule"></div>
      <p class="program">To administer their<br><span class="accent">Rental Registration Program</span></p>
    </div>
    <div class="front-divider"></div>
    <div class="front-photo" role="img" aria-label="Photo of a brick house with a gray roof under a blue sky"></div>
    <div class="community-logo">LOGO</div>
    <div class="front-footer"><span>For more info to resolve this matter go to;</span><span class="url">www.veltridane.example</span></div>
  </section>

  <section class="postcard postcard--back" aria-label="Postcard back">
    <div class="back-photo" role="img" aria-label="Faded photo of a white house front"></div>
    <div class="address-fields">
      <div class="field field--property"><span>Property Requiring Registeration :</span></div>
      <ol class="property-list">
        <li><span class="num">1.</span><span class="rule"></span></li>
        <li><span class="num">2.</span><span class="rule"></span></li>
        <li><span class="num">3.</span><span class="rule"></span></li>
        <li><span class="num">4.</span><span class="rule"></span></li>
        <li><span class="num">5.</span><span class="rule"></span></li>
      </ol>
      <div class="field field--owner"><span>Owner's Name:</span><span class="rule"></span></div>
      <div class="field field--site"><span>Site Address:</span><span class="rule"></span></div>
      <div class="field field--id"><span>Property ID:</span><span class="rule"></span></div>
      <div class="field field--notice"><span>Notification:</span><span class="rule"></span></div>
    </div>
    <div class="back-side" role="img" aria-label="Yellow-tinted photo of a house roofline"></div>
    <div class="stamp-box"></div>
    <div class="back-footer">
      if you are having problems with the above link you can contact veltridane<br>
      by calling <span class="contact">(555) 014-2387</span> or emailing <span class="contact">support@VELTRIDANE.EXAMPLE</span>
    </div>
  </section>
</body>
</html>
```